website re-design - the brisk loft

The Brisk Loft is an existing website that we built using a new zealand based online CMS tool which is quite flexible and accomodates custom designs. You can check it here: http://www.pagecrafter.co.nz/.

We have a logo already and the content on the website is OK.
The website can be found at www.thebriskloft.com.au

mainly the homepage, but if the design is easily adapted to the other pages then, we will commission the winner to update these pages also.
Updates

Hi there,  I am uploading an image to be used as the main image on the homepage design,  so all submissions have the same image.

Target Market(s)

property developers, architects, builders, home buyers

Industry/Entity Type

Shop

Requirements
Must have
• Must utilise the existing CMS or at least be compatible to upload
Nice to have
• a promotional banner that can be turned off and on and changed as required as we offer different promotions over time.

```html
<!DOCTYPE html>
<html lang="en">
<head>
<meta charset="utf-8">
<title>The Brisk Loft – Architectural Scale Models</title>
<link href="https://fonts.googleapis.com/css2?family=Arimo:wght@400;700&family=Questrial&family=Lora:ital,wght@1,400;1,700&display=swap" rel="stylesheet">
<style>
:root{
  --orange:#e8761c;
  --orange-dark:#c8400f;
  --ink:#222;
  --grey-text:#555;
  --line:#dcdcdc;
  --band:#ececec;
  --footer:#151515;
  --footer-text:#cfcfcf;
}
*{box-sizing:border-box;margin:0;padding:0}
html,body{width:943px;height:1200px;overflow:hidden;background:#fff}
body{position:relative;font-family:"Arimo",Arial,sans-serif;color:var(--ink)}
.abs{position:absolute}

.top-rule{left:0;top:0;width:943px;height:6px;background:var(--orange)}
.call-tab{left:656px;top:0;width:239px;height:24px;background:var(--orange);border-radius:0 0 14px 14px;color:#fff;font-weight:700;font-size:13px;text-align:center;line-height:24px;letter-spacing:.3px}

.brand-mark{left:262px;top:34px;width:118px;height:82px;border:5px solid var(--orange);border-radius:4px}
.brand-name{left:417px;top:50px;font-family:"Questrial",sans-serif;font-size:37px;color:#4a4a4a;letter-spacing:-.5px}
.brand-tag{left:419px;top:88px;font-family:"Questrial",sans-serif;font-size:18.5px;color:var(--orange);letter-spacing:.4px}

.nav{left:0;top:145px;width:943px;height:41px;background:linear-gradient(#fff,#f1f1f1);border-top:1px solid #e4e4e4;border-bottom:3px solid var(--orange)}
.nav ul{list-style:none;display:flex;position:absolute;left:44px;top:0;height:38px}
.nav li{font-size:13.5px;color:#333;line-height:38px;padding:0 14px;border-right:1px solid #d8d8d8;white-space:nowrap}
.nav li:last-child{border-right:none}
.nav li.active{background:var(--orange);color:#fff;width:75px;text-align:center;padding:0}
.nav li:nth-child(2){padding:0 18px 0 14px}

.hero-frame{left:44px;top:205px;width:856px;height:312px;background:#fff;border:1px solid #ccc;box-shadow:0 1px 4px rgba(0,0,0,.2);padding:5px}
.hero-photo{width:100%;height:100%;background:linear-gradient(135deg,#7d7a78 0%,#9a9491 30%,#5d6a55 55%,#8d8b86 80%,#6f706c 100%)}
.hero-caption{left:630px;top:236px;width:230px;height:249px;background:rgba(40,40,40,.82);padding:14px 14px;color:#fff}
.hero-caption h2{font-family:"Lora",serif;font-style:italic;font-weight:400;color:var(--orange);font-size:23px;line-height:27px;margin-bottom:10px}
.hero-caption p{font-size:12.5px;line-height:20px}

.thumb-band{left:0;top:538px;width:943px;height:80px;background:linear-gradient(#f6f6f6,#e3e3e3);border-top:1px solid #ddd;border-bottom:1px solid #ddd}
.thumb{top:547px;width:121px;height:60px;background:linear-gradient(#a9a49d,#7f7a6f 60%,#6e8a55);border:1px solid #bbb}
.arrow{top:560px}

.main-quote{left:44px;top:656px;width:563px;text-align:center;font-family:"Lora",serif;font-style:italic;font-size:19px;color:#333}
.copy{left:44px;width:563px;font-size:11px;line-height:21px;color:var(--grey-text)}
.copy .yes{color:var(--orange)}
.questions{left:50px;top:796px;width:560px;list-style:none}
.questions li{position:relative;padding-left:30px;font-size:11.5px;font-weight:700;line-height:16px;color:#333;margin-bottom:10px}
.questions li::before{content:"";position:absolute;left:2px;top:3px;width:10px;height:10px;border-radius:50%;background:#f2d6c4;box-shadow:inset 0 0 0 3px #fbeee5;border:1px solid #e5b894}

.call-box{left:44px;top:999px;width:202px;height:72px;border:1px solid #ccc;border-radius:4px;background:linear-gradient(#fff,#e9e9e9)}
.call-box .label{position:absolute;right:12px;top:10px;font-size:13.5px;color:#333;letter-spacing:.5px}
.call-box .num{position:absolute;right:10px;top:36px;font-size:17px;color:#333}
.call-box svg{position:absolute;left:6px;top:12px}

.testimonial{left:267px;top:999px;width:340px;height:73px;border:1px solid #d4d4d4;background:#fff}
.testimonial .mark{position:absolute;left:8px;top:2px;font-family:"Lora",serif;font-size:40px;color:#ddd}
.testimonial p{position:absolute;left:46px;top:10px;right:12px;font-size:10.5px;line-height:15px;color:#777}
.testimonial-tail{left:540px;top:1071px}
.testimonial-name{left:493px;top:1076px;font-family:"Lora",serif;font-style:italic;font-size:15px;color:var(--orange)}

.divider{left:631px;top:638px;width:1px;height:470px;background:var(--line)}
.side-title{left:649px;top:645px;font-size:15px;color:#222;letter-spacing:.3px}
.step{left:653px;width:250px;font-size:11.5px;font-weight:700;line-height:18px;color:#333;padding-left:36px}
.step .n{position:absolute;left:0;top:0;width:20px;height:20px;border-radius:50%;background:var(--orange);color:#fff;font-size:11px;text-align:center;line-height:20px}
.btn{left:653px;width:228px;height:43px;font-size:12px;font-weight:700;text-align:center;line-height:43px}
.btn-quote{top:752px;background:linear-gradient(90deg,var(--orange),var(--orange-dark));color:#fff;border-radius:2px}
.btn-order{top:812px;background:linear-gradient(#fff,#ececec);color:#333;border:1px solid #d4d4d4;box-shadow:0 2px 3px rgba(0,0,0,.12)}
.side-copy{left:649px;width:252px;font-size:10.5px;line-height:17px;color:var(--grey-text)}

.share{top:1063px;height:18px;display:flex}
.share .btn-s{width:28px;height:18px;border:1px solid #b8c4d6;background:linear-gradient(#fff,#dfe6ef);border-radius:2px}
.share .cnt{height:18px;border:1px solid #ccc;background:#fff;font-size:10px;line-height:16px;padding:0 6px;color:#444;margin-left:3px}

.footer{left:0;top:1127px;width:943px;height:73px;background:var(--footer)}
.footer-links{left:44px;top:1143px;font-size:10px;color:var(--footer-text);word-spacing:1px}
.footer-links span{margin:0 8px;color:#888}
.footer-copy{left:44px;top:1167px;font-size:9.5px;color:#888}
.footer-sq{top:1142px;width:15px;height:15px;background:#555;border-radius:2px}
</style>
</head>
<body>
<div class="abs top-rule"></div>
<div class="abs call-tab">CALL US: (08) 5550 0147</div>

<div class="abs brand-mark"></div>
<div class="abs brand-name">THE BRISK LOFT</div>
<div class="abs brand-tag">ARCHITECTURAL SCALE MODELS</div>

<nav class="abs nav">
  <ul>
    <li class="active">HOME</li><li>GALLERY</li><li>ORDER ONLINE</li><li>GET A QUOTE</li><li>CONTACT US</li><li>3D VISUALISATION</li><li>ABOUT US</li><li>SITE MAP</li>
  </ul>
</nav>

<div class="abs hero-frame"><div class="hero-photo" role="img" aria-label="Aerial view of an architectural scale model of a townhouse development with trees and roads"></div></div>
<div class="abs hero-caption">
  <h2>Lorem ipsum dolor sit amet,</h2>
  <p>Lorem ipsum dolor sit amet, consectetuer adipiscing elit. Aenean commodo ligula eget dolor. Aenean massa. Cum sociis natoque penatibus et magnis dis parturient montes, nascetur ridiculus mus.</p>
</div>

<div class="abs thumb-band"></div>
<svg class="abs arrow" style="left:57px" width="30" height="34" viewBox="0 0 30 34"><path d="M26 3 L8 17 L26 31 L20 17 Z" fill="#e8761c"/></svg>
<div class="abs thumb" style="left:105px" role="img" aria-label="Scale model of a two-storey house"></div>
<div class="abs thumb" style="left:257px" role="img" aria-label="Scale model of a two-storey house"></div>
<div class="abs thumb" style="left:409px" role="img" aria-label="Scale model of a two-storey house"></div>
<div class="abs thumb" style="left:561px" role="img" aria-label="Scale model of a two-storey house"></div>
<div class="abs thumb" style="left:712px" role="img" aria-label="Scale model of a two-storey house"></div>
<svg class="abs arrow" style="left:854px" width="30" height="34" viewBox="0 0 30 34"><path d="M4 3 L22 17 L4 31 L10 17 Z" fill="#fff" stroke="#c8c8c8"/></svg>

<div class="abs main-quote">" a picture's worth a thousand words... a model says it all..."</div>
<p class="abs copy" style="top:693px">Getting an architectural model produced can be expensive and time consuming, but it can also add a lot of value to a project.&nbsp; A scale model lets everyone involved, get a very clear understanding of your building.</p>
<p class="abs copy" style="top:757px">If you answered <span class="yes">yes</span> to any of the following questions, then you should be using the brisk loft.</p>
<ul class="abs questions">
  <li>Are you undertaking a new apartment development or land development and need a model for council approval or marketing purposes?</li>
  <li>Are you getting a new house designed and built and need a clear understanding of how it will look?</li>
  <li>Are you an architect or building designer looking for a more affordable way to add to your service?</li>
  <li>Are you wanting to clarify in your own mind how your new building sits on its site?</li>
  <li>Are you looking to for a way to market your buildings in an effective and affordable format that everyone can relate to?</li>
</ul>

<div class="abs call-box">
  <svg width="78" height="50" viewBox="0 0 78 50" aria-hidden="true">
    <path d="M4 14 Q39 -4 74 14 L70 22 L56 20 L54 13 Q39 8 24 13 L22 20 L8 22 Z" fill="#1b1b1b"/>
    <path d="M20 26 L58 26 L66 48 L12 48 Z" fill="#2a2a2a"/>
    <circle cx="39" cy="37" r="7" fill="#555"/>
  </svg>
  <div class="label">CALL US</div>
  <div class="num">(08) 5550 0147</div>
</div>

<div class="abs testimonial">
  <div class="mark">“</div>
  <p>Lorem ipsum dolor sit amet, consectetuer adipiscing elit. Aenean commodo ligula eget dolor. Aenean massa. Cum sociis natoque penatibus et magnis</p>
</div>
<svg class="abs testimonial-tail" width="34" height="16" viewBox="0 0 34 16"><path d="M0 1 L34 1 L4 15 Z" fill="#fff" stroke="#d4d4d4"/><rect x="1" y="0" width="32" height="2" fill="#fff"/></svg>
<div class="abs testimonial-name">Mara</div>

<div class="abs divider"></div>
<div class="abs side-title">IT'S THIS EASY</div>
<div class="abs step" style="top:674px"><span class="n">1</span>Order online or fill in the quote form.</div>
<div class="abs step" style="top:699px"><span class="n">2</span>We'll build your model and deliver it right to your door.</div>
<div class="abs btn btn-quote">Click here to get a Quote.</div>
<div class="abs btn btn-order">Click here to Order your Model Now.</div>
<p class="abs side-copy" style="top:876px">You can tailor your model to suit your project and budget needs.&nbsp; There are various add-ons such as a display case, internal walls, acrylic windows, people trees and cars and site contours as well as a scaled pricing structure based on the size of your building.</p>
<p class="abs side-copy" style="top:978px">We have made the system very easy to use, so all you need to do is click your way to your new scale model.&nbsp; Just follow the prompts and away you go.</p>

<div class="abs share" style="left:653px"><div class="btn-s"></div><div class="cnt">652</div></div>
<div class="abs share" style="left:731px"><div class="btn-s" style="width:36px"></div><div class="cnt">21</div></div>
<div class="abs share" style="left:812px"><div class="btn-s" style="width:46px"></div><div class="cnt">0</div></div>

<footer class="abs footer"></footer>
<div class="abs footer-links">Home<span>|</span>Gallery<span>|</span>Order Online<span>|</span>Get a Quote<span>|</span>Contact Us<span>|</span>3d Visualisation<span>|</span>About US<span>|</span>Site map</div>
<div class="abs footer-copy">© Copyright The Brisk Loft | Terms &amp; Conditions | Phone: (08) 5550 0147 Australia</div>
<div class="abs footer-sq" style="left:858px"></div>
<div class="abs footer-sq" style="left:878px"></div>
</body>
</html>
```